Gourmet Restaurant take out menu

We need a take out menu design that is trendy for a casual upscale Italian restaurant with a vast menu. This menu must be able to be 4 color and reproducible in large quantities to be bulked mailed or inserted into a daily paper. It must also maintain a theme that can be crossed over to our in house dining menu and specials menu.
OUR WEBSITE:
www.velmorabistrohouse.example
For the content, go to the Menu section of our website. We are interested in the design scheme and a template to use.
Target Market(s)
families, sinle individuals seeking take out meals and delivery
Industry/Entity Type
Restaurant

```html
<!DOCTYPE html>
<html lang="en">
<head>
<meta charset="utf-8">
<title>Take Out Menu</title>
<link href="https://fonts.googleapis.com/css2?family=Noto+Serif:wght@400;700&family=Raleway:wght@300;400&display=swap" rel="stylesheet">
<style>
:root{
  --page:#ececec;
  --paper:#dccaa6;
  --paper-dark:#cfbd99;
  --red:#8f2a1b;
  --ink:#2a2320;
  --soft:#6a5a4c;
}
*{margin:0;padding:0;box-sizing:border-box}
html,body{width:1200px;height:795px;overflow:hidden;background:var(--page)}
body{position:relative;font-family:"Noto Serif",serif;color:var(--ink)}
.menu{position:absolute;left:45px;top:4px;width:1110px;height:787px;display:flex}
.panel{position:relative;height:100%;background:var(--paper)}
.panel-left{width:376px;border-right:1px solid #b9a887}
.panel-middle{width:370px;border-right:1px solid #b9a887}
.panel-right{width:364px;background:var(--paper-dark)}
.rule{position:absolute;height:1.5px;background:var(--red)}
.vrule{position:absolute;width:1.5px;background:var(--red)}
.heading{position:absolute;left:0;right:0;text-align:center;font-weight:700;font-size:27px;letter-spacing:.3px}
.heading-rule{position:absolute;height:1.5px;background:var(--red)}
.ornament{position:absolute;background:rgba(143,42,27,.28);border-radius:10px}
.toppings-label{position:absolute;left:0;right:0;text-align:center;font-size:15px}
.toppings{position:absolute;font-family:"Raleway",sans-serif;font-size:10.5px;line-height:20px;text-transform:uppercase;letter-spacing:.1px;white-space:nowrap;text-align:center}
.item{position:absolute;left:0;right:0;padding:0 26px 0 40px}
.item-row{display:flex;justify-content:space-between;align-items:baseline}
.item-name{font-weight:700;font-size:13px;text-transform:uppercase;letter-spacing:.2px}
.item-price{font-size:8.5px}
.item-desc{font-family:"Raleway",sans-serif;font-size:9.5px;color:var(--soft);line-height:11px;margin-top:5px}
.item.featured .item-row{background:var(--red);color:#f1e3cb;padding:3px 10px;margin:0 -26px 0 -14px}
.item.featured .item-name{font-weight:400}
.panel-middle .item{padding:0 24px 0 24px}
.panel-middle .item.featured .item-row{margin:0 -14px 0 -24px;padding:3px 14px 3px 24px}
.panel-right .item{padding:0 26px 0 20px}
.panel-right .item.featured .item-row{margin:0 -26px 0 -20px;padding:3px 26px 3px 20px}
.small-table{position:absolute;display:grid;font-size:6.5px;font-weight:700;line-height:13px}
.small-table .price{text-align:right}
.subhead{position:absolute;left:0;right:0;text-align:center;font-size:6.5px;text-transform:uppercase}
.bev{position:absolute;font-family:"Raleway",sans-serif;font-size:8px;line-height:10px;text-align:center}
.bev-price{position:absolute;font-size:9px}
.dash{position:absolute;border-top:1.5px dashed var(--red);height:0}
</style>
</head>
<body>
<div class="menu">

  <section class="panel panel-left">
    <div class="rule" style="left:0;right:0;top:20px"></div>
    <h2 class="heading" style="top:48px">GOURMENT PIZZA</h2>
    <div class="heading-rule" style="left:50px;right:24px;top:92px"></div>
    <p class="toppings-label" style="top:107px">Toppings for 1.99</p>
    <div class="ornament" role="img" aria-label="Scroll flourish" style="left:38px;top:165px;width:14px;height:112px"></div>
    <div class="ornament" role="img" aria-label="Scroll flourish" style="left:334px;top:165px;width:14px;height:112px"></div>
    <p class="toppings" style="top:150px;left:70px;width:250px">
      Ham • Broccoli • Extra Cheese<br>
      Tomatoes hot or sweet peppers<br>
      • Roasted peppers • Pepperoni •<br>
      Spinach • Italian sausage • Onions<br>
      • Black olives • Green peppers •<br>
      Mushrooms • Grilled chicken<br>
      Meatball bacon and ricotta 3.00
    </p>
    <div class="item" style="top:326px"><div class="item-row"><span class="item-name">Plain Cheese</span><span class="item-price">8.99/11.99/12.99</span></div></div>
    <div class="item" style="top:357px"><div class="item-row"><span class="item-name">Traditional White</span><span class="item-price">8.59/11.59/13.99</span></div><p class="item-desc">Olive oil, garlic, mozzarella cheese</p></div>
    <div class="item" style="top:406px"><div class="item-row"><span class="item-name">Chicken Bacon Ranch</span><span class="item-price">10.99/14.99/16.99</span></div><p class="item-desc">Garlic chicken, bacon, pepperjack and cheddar cheese,<br>red onions, diced tomatoes, drizzle of ranch dressing</p></div>
    <div class="item" style="top:469px"><div class="item-row"><span class="item-name">Bronx Bomber</span><span class="item-price">11.99/14.99/16.99</span></div><p class="item-desc">Sausage, prosciutto ham, oregano, crumbled bleu and mozzarella<br>cheese</p></div>
    <div class="item" style="top:539px"><div class="item-row"><span class="item-name">Buffalo Chicken</span><span class="item-price">10.99/14.99/16.99</span></div><p class="item-desc">Buffalo sauce, chicken, mozzarella cheese, side of bleu cheese<br>dressing</p></div>
    <div class="item featured" style="top:600px"><div class="item-row"><span class="item-name">Gourment Special</span><span class="item-price">12.99/16.99/18.99</span></div><p class="item-desc">Buffalo sauce, chicken, mozzarella cheese, side of bleu cheese<br>dressing</p></div>
    <div class="item" style="top:668px"><div class="item-row"><span class="item-name">Margarita</span><span class="item-price">8.99/11.99/13.99</span></div><p class="item-desc">Fresh basil, tomato, buffalo mozzarella cheese</p></div>
    <div class="dash" style="left:156px;width:70px;top:730px"></div>
    <div class="rule" style="left:34px;right:26px;top:755px"></div>
  </section>

  <section class="panel panel-middle">
    <div class="rule" style="left:0;right:0;top:27px"></div>
    <div class="vrule" style="left:0;top:50px;height:735px"></div>
    <div class="vrule" style="right:0;top:50px;height:735px"></div>
    <div class="item" style="top:80px"><div class="item-row"><span class="item-name">Roasted Vegetable</span><span class="item-price">11.99/14.99/16.99</span></div><p class="item-desc">Eggplant, red and yellow peppers, onions, artichokes, Kalamata olives,<br>tomatoes, mozzarella cheese. Veggie Lover Olive oil, garlic, broccoli,<br>spinach, tomato, mozzarella cheese</p></div>
    <div class="item featured" style="top:157px"><div class="item-row"><span class="item-name">Sweet Hawaiian</span><span class="item-price">11.99/14.99/16.99</span></div><p class="item-desc">Pineapple, tomatoes, ham, mozzarella cheese</p></div>
    <div class="item" style="top:213px"><div class="item-row"><span class="item-name">Spinach and Artichoke</span><span class="item-price">8.99/11.99/12.99</span></div><p class="item-desc">Spinach, artichoke hearts, basil, mozzarella, parmesan cheese</p></div>
    <div class="item" style="top:274px"><div class="item-row"><span class="item-name">Philly Chease Steak</span><span class="item-price">11.99/14.99/16.99</span></div><p class="item-desc">Philly steak, green peppers, onions, provolone, American cheese</p></div>
    <div class="item" style="top:336px"><div class="item-row"><span class="item-name">Grandma`s Pie</span><span class="item-price">14.99</span></div><p class="item-desc">Thin crust pizza topped with mozzarella,<br>tomato sauce, buffalo mozzarella, fresh basil, olive oil. (One Size)</p></div>
    <h2 class="heading" style="top:414px">LUNCH ABILITIES</h2>
    <div class="heading-rule" style="left:30px;right:24px;top:458px"></div>
    <p class="subhead" style="top:470px">A smaller portion of some of your gourmet favorites</p>
    <div class="vrule" style="left:184px;top:488px;height:90px;width:1px"></div>
    <div class="small-table" style="left:24px;top:496px;width:150px;grid-template-columns:1fr 30px">
      <span>Baked Penne Pasta</span><span class="price">7.99</span>
      <span>Chicken Parmigiana</span><span class="price">8.99</span>
      <span>Chicken Rosa</span><span class="price">8.99</span>
      <span>Eggplant Parmigiana</span><span class="price">8.99</span>
      <span>Chicken Francaise</span><span class="price">8.99</span>
    </div>
    <div class="small-table" style="left:196px;top:496px;width:150px;grid-template-columns:1fr 30px">
      <span>Penne Italiano</span><span class="price">8.99</span>
      <span>Linguini and Clams</span><span class="price">8.99</span>
      <span>Add a House Salad or</span><span class="price"></span>
      <span>Cup of Soup Du Jour</span><span class="price">2.99</span>
    </div>
    <div class="rule" style="left:24px;right:24px;top:580px"></div>
    <div class="dash" style="left:24px;width:62px;top:606px"></div>
    <h2 class="heading" style="top:587px">BEVERAGES</h2>
    <div class="dash" style="left:284px;width:62px;top:606px"></div>
    <span class="bev-price" style="left:66px;top:644px">1.99</span>
    <p class="bev" style="left:90px;width:190px;top:641px">16 oz Bottled Tea<br>Home-Brewed Iced Tea<br>20 oz Bottles (Pelton Cola, Diet Pelton, Orange,<br>Ginger Ale, Cedar Fizz, Burl Root Beer)</p>
    <span class="bev-price" style="left:294px;top:644px">1.99</span>
    <div class="dash" style="left:0;width:56px;top:697px"></div>
    <span class="bev-price" style="left:66px;top:701px">2.99</span>
    <p class="bev" style="left:90px;width:190px;top:698px">2 Liter Bottles (Pelton Cola, Diet Pelton, Orange,<br>Ginger Ale, Cedar Fizz, Burl Root Beer)</p>
    <span class="bev-price" style="left:294px;top:701px">2.99</span>
    <p class="bev" style="left:90px;width:190px;top:724px">16 oz Bottled Water<br><span style="font-size:9px;line-height:12px">1.59</span></p>
    <div class="rule" style="left:24px;right:24px;top:753px"></div>
  </section>

  <section class="panel panel-right">
    <div class="ornament" role="img" aria-label="Swirl flourish" style="left:108px;top:18px;width:116px;height:16px"></div>
    <h2 class="heading" style="top:50px">GHILDRENS MENU</h2>
    <div class="heading-rule" style="left:0;right:30px;top:93px"></div>
    <div class="small-table" style="left:20px;top:106px;width:140px;grid-template-columns:1fr 24px;font-size:5.6px">
      <span>Cheeseburger and Fries</span><span class="price">5.99</span>
      <span>Chicken Fingers and Fries</span><span class="price">6.59</span>
      <span>Grilled Cheese and Fries</span><span class="price">5.99</span>
      <span>Grilled Chicken Breast</span><span class="price"></span>
      <span>with Buttered Pasta</span><span class="price">6.99</span>
    </div>
    <div class="small-table" style="left:180px;top:104px;width:144px;grid-template-columns:1fr 24px;font-size:5.6px">
      <span>Linguini and Meatball</span><span class="price">6.99</span>
      <span>Mac and Cheese</span><span class="price">4.99</span>
      <span>Mini Pizza</span><span class="price">5.99</span>
      <span>Ravioli and Meatball</span><span class="price">6.99</span>
      <span>Sliders (2) and Fries</span><span class="price">5.99</span>
    </div>
    <h2 class="heading" style="top:212px">AWESOME BURGERS</h2>
    <div class="heading-rule" style="left:180px;right:30px;top:256px"></div>
    <div class="heading-rule" style="left:20px;width:110px;top:256px"></div>
    <div class="item" style="top:282px"><div class="item-row"><span class="item-name">Cheese Burger</span><span class="item-price">7.99</span></div></div>
    <div class="item" style="top:312px"><div class="item-row"><span class="item-name">Bacon Cheddar</span><span class="item-price">8.99</span></div><p class="item-desc">Applewood smoked bacon, sharp cheddar</p></div>
    <div class="item" style="top:366px"><div class="item-row"><span class="item-name">Blue Cheese BLT</span><span class="item-price">9.59</span></div><p class="item-desc">Bacon, lettuce, tomato, onion, mayonnaise, bleu cheese</p></div>
    <div class="item" style="top:417px"><div class="item-row"><span class="item-name">California</span><span class="item-price">9.99</span></div><p class="item-desc">Avocado, roasted green chilies, pepper jack cheese, chipotle<br>mayo, ranch dressing</p></div>
    <div class="item featured" style="top:477px"><div class="item-row"><span class="item-name">Gourment Sliders</span><span class="item-price">8.99</span></div><p class="item-desc">5 bite-sized burgers with American cheese on mini potato rolls</p></div>
    <div class="item" style="top:536px"><div class="item-row"><span class="item-name">Mushroom Swiss</span><span class="item-price">8.59</span></div><p class="item-desc">Sautéed mushrooms, onions and mayo topped with Swiss cheese</p></div>
    <div class="item" style="top:584px"><div class="item-row"><span class="item-name">Portabella</span><span class="item-price">8.59</span></div><p class="item-desc">Angus burger, roasted portabella, melted provolone cheese</p></div>
    <div class="item" style="top:631px"><div class="item-row"><span class="item-name">Pub</span><span class="item-price">9.99</span></div><p class="item-desc">Keystone steak sauce and mayo, topped with onion rings, bleu cheese</p></div>
    <div class="item" style="top:689px"><div class="item-row"><span class="item-name">Smokehouse Barbecue</span><span class="item-price">9.99</span></div><p class="item-desc">Smoked bacon, melted cheddar cheese, crispy onion strings,<br>tangy barbecue-ranch sauce</p></div>
  </section>

</div>
</body>
</html>
```